Homepage Design for Digital Advertising Company

The website will be very simple, with just one page (the homepage).

We are a new startup company, Quorvane Media, and focus on social media and gaming advertising. We work directly with brands, and with other media agencies. I have attached some details about our company, what we do, and content you can use for the website. I have also attached a screenshot of our logo (high quality files will be provided shortly).

This is an example of a website we really like. They do not do what we do, however their layout is great, and the best part about it is that they really get the message accross of exactly what they do as soon as the page loads. We do not have a product video, so that part does not apply, however i love their basic page layout.
http://www.plindero.com/

We can say something like this:
Simple Social Media and Gaming Advertising (BIG TEXT)
WE DELIVER: Brellows fans and likes, Chirrup followers, Targeted ads and video, and more... (SubText)

On the homepage, we want to have a prominent "Free Consultation" box with a "Submit" button. This box will have input boxes for:
Name
Email
Phone
Or, we can do just a simple email submit as seen here (I like how they did a one long page design BTW)
http://morvexa.com/

Here are some other sites i like:
http://www.talvicor.com/
http://www.gremblo.com/
http://torvanix.net/

Not sure what you will get out of this one, but its too unique to not mention:
http://yuvasi.com/handset/

COLORS:
We are flexible on color scheme. We can change the color of the logo, so dont let that limit your color concepts.

Content on site:
We can use fly out buttons or "more" links for extra text dropdowns if you only want to include an excerpt from each topic in the attached content sheet. Dont want page to be too busy.

Long One Page:
We are not opposed to something like this, by the way
http://morvexa.com/

Target Market(s)

big brands, advertising agencies

Industry/Entity Type

Digital

Requirements
Must have
• Logo
Sign up form
Nice to have
• all the content from our attachment
Should not have
• busy designs, lack of white space, too much text

```html
<!DOCTYPE html>
<html lang="en">
<head>
<meta charset="utf-8">
<title>Quorvane Media</title>
<link rel="stylesheet" href="https://fonts.googleapis.com/css2?family=Open+Sans:wght@400;600;700&family=PT+Sans:wght@400;700&display=swap">
<style>
  :root {
    --bg-light: #f8f8f8;
    --bg-mid: #e4e4e4;
    --ink: #262626;
    --ink-soft: #444;
    --brand-blue: #0a66b0;
    --nav-blue: #1d4f9a;
    --button-blue: #0a7de0;
    --button-blue-dark: #0560b8;
    --rule: #cfcfcf;
    --panel-border: #ffffff;
    --share-deep: #4a63a8;
    --share-light: #7fd0ea;
  }
  * { margin: 0; padding: 0; box-sizing: border-box; }
  html, body { width: 1200px; height: 857px; overflow: hidden; }
  body {
    position: relative;
    font-family: "Open Sans", sans-serif;
    color: var(--ink);
    background: radial-gradient(ellipse 700px 520px at 760px 360px, var(--bg-light) 0%, #eeeeee 55%, var(--bg-mid) 100%);
  }
  .main-nav { position: absolute; top: 23px; left: 20px; height: 28px; }
  .main-nav a {
    position: absolute; top: 0; height: 28px; line-height: 28px;
    font-family: "PT Sans", sans-serif; font-size: 19px; color: var(--nav-blue);
    text-decoration: none; white-space: nowrap;
  }
  .main-nav .is-current {
    left: 0; width: 83px; text-align: center;
    border: 1px solid #bdbdbd; border-radius: 6px;
    background: linear-gradient(#ffffff, #ececec);
  }
  .main-nav .sep { position: absolute; top: -4px; width: 1px; height: 34px; background: var(--rule); }
  .call-line {
    position: absolute; top: 16px; right: 32px; display: flex; align-items: center; gap: 8px;
    font-size: 24px; color: #4a4a4a;
  }
  .call-line strong { font-weight: 700; color: #3a3a3a; }
  .brand-name {
    position: absolute; left: 37px; top: 150px;
    font-size: 43px; font-weight: 400; color: var(--ink); letter-spacing: -0.5px;
  }
  .hero-lead { position: absolute; left: 27px; top: 232px; font-size: 27px; font-weight: 400; color: #333; letter-spacing: -0.3px; }
  .hero-title {
    position: absolute; left: 25px; top: 270px;
    font-size: 64px; font-weight: 700; line-height: 70px; letter-spacing: -1.5px;
  }
  .hero-title .blue { color: var(--brand-blue); display: block; }
  .hero-title .dark { color: var(--ink); display: block; }
  .hero-sub {
    position: absolute; left: 28px; top: 486px; width: 700px;
    font-size: 15px; color: var(--ink-soft);
  }
  .hero-sub strong { color: var(--brand-blue); font-weight: 700; }
  .btn {
    position: absolute; top: 526px; height: 44px; border-radius: 5px; border: 0;
    font-family: "PT Sans", sans-serif; font-size: 18px; line-height: 44px; text-align: center; text-decoration: none;
  }
  .btn-primary {
    left: 35px; width: 179px; color: #fff;
    background: linear-gradient(var(--button-blue), var(--button-blue-dark));
  }
  .consult-form { position: absolute; left: 251px; top: 526px; display: flex; gap: 8px; }
  .consult-form input {
    width: 300px; height: 44px; padding: 0 14px; border-radius: 5px;
    border: 1px solid #cfcfcf; background: #fff;
    font-family: "PT Sans", sans-serif; font-size: 16px; color: #444;
    box-shadow: inset 0 1px 3px rgba(0,0,0,.08);
  }
  .consult-form button {
    height: 44px; width: 110px; border-radius: 5px; cursor: pointer;
    font-family: "PT Sans", sans-serif; font-size: 18px; color: #444;
    background: linear-gradient(#fafafa, #e2e2e2); border: 1px solid #cfcfcf;
    box-shadow: 0 1px 3px rgba(0,0,0,.15);
  }
  .decor-line { position: absolute; left: 0; top: 0; pointer-events: none; }
  .contact-panel {
    position: absolute; left: 93px; top: 644px; width: 1014px; height: 151px;
    border: 1px solid var(--panel-border); border-radius: 7px;
    background: linear-gradient(rgba(255,255,255,.55), rgba(245,245,245,.35));
    box-shadow: 0 0 0 1px #dddddd;
  }
  .contact-panel .divider {
    position: absolute; top: 14px; width: 2px; height: 122px;
    background: linear-gradient(transparent, #cccccc 30%, #cccccc 70%, transparent);
  }
  .panel-heading { position: absolute; left: 21px; top: 12px; font-size: 21px; font-weight: 400; color: #3a3a3a; }
  .handset-art {
    position: absolute; left: 37px; top: 48px; width: 30px; height: 58px; border-radius: 5px;
    background: linear-gradient(#555, #111);
  }
  .talk-label { position: absolute; left: 78px; top: 43px; font-size: 13px; color: var(--brand-blue); }
  .contact-label { position: absolute; font-size: 15px; font-weight: 600; color: #444; }
  .contact-value { position: absolute; font-family: "PT Sans", sans-serif; font-size: 14px; letter-spacing: 1px; color: #444; }
  .mail-art {
    position: absolute; left: 353px; top: 56px; width: 50px; height: 42px; border-radius: 4px;
    background: linear-gradient(#5cc8e8, #1f8fc0);
  }
  .share-row { position: absolute; left: 683px; display: flex; align-items: center; gap: 18px; }
  .share-btn {
    width: 84px; height: 27px; border-radius: 2px; color: #fff;
    font-family: "PT Sans", sans-serif; font-size: 12px; line-height: 27px; text-align: center; letter-spacing: .5px;
    box-shadow: 0 1px 2px rgba(0,0,0,.3);
  }
  .share-btn.deep { background: linear-gradient(#6a82c4, var(--share-deep)); }
  .share-btn.light { background: linear-gradient(#a5e2f3, var(--share-light)); }
  .share-text { font-family: "PT Sans", sans-serif; font-size: 14px; letter-spacing: 1px; color: #444; }
  .site-footer {
    position: absolute; left: 0; width: 1200px; top: 827px; text-align: center;
    font-family: "PT Sans", sans-serif; font-size: 12px; color: #444; letter-spacing: .2px;
  }
</style>
</head>
<body>

<svg class="decor-line" width="1200" height="857" aria-hidden="true">
  <line x1="250" y1="650" x2="1030" y2="140" stroke="#c9c9c9" stroke-width="1"/>
</svg>

<nav class="main-nav">
  <a class="is-current" href="#">Home</a>
  <span class="sep" style="left:89px"></span>
  <a href="#" style="left:109px">About Us</a>
  <span class="sep" style="left:204px"></span>
  <a href="#" style="left:229px">Support</a>
  <span class="sep" style="left:314px"></span>
  <a href="#" style="left:340px">FAQ's</a>
  <span class="sep" style="left:412px"></span>
  <a href="#" style="left:439px">Testimonials</a>
  <span class="sep" style="left:566px"></span>
  <a href="#" style="left:594px">Blog</a>
</nav>

<div class="call-line">
  <svg width="34" height="34" viewBox="0 0 34 34" aria-hidden="true">
    <circle cx="17" cy="17" r="15" fill="none" stroke="#3a3a3a" stroke-width="2"/>
    <path d="M12 9c1-1 2-1 3 0l1.5 3c.4 1-.2 1.6-1 2.2 1 2 2.4 3.4 4.3 4.3.6-.8 1.3-1.4 2.2-1l3 1.5c1 .5 1 2 0 3-1.5 1.5-3.5 2-6 .6-3.4-1.9-6-4.5-7.8-7.9C9.8 12.5 10.5 10.5 12 9z" fill="#3a3a3a"/>
  </svg>
  <span>Call: <strong>1-555-204-7731</strong></span>
</div>

<div class="brand-name">Quorvane Media</div>

<p class="hero-lead">For big brands and media agencies, it is simple</p>
<h1 class="hero-title">
  <span class="blue">Simple Social Media</span>
  <span class="dark">and Gaming</span>
  <span class="blue">ADVERTISING</span>
</h1>
<p class="hero-sub"><strong>WE DELIVER:</strong> Brellows fans and likes, Chirrup followers, targeted ads and video, and more...</p>

<a class="btn btn-primary" href="#">More info Click here</a>
<form class="consult-form" action="#">
  <input type="email" name="email" placeholder="Email for a Free Consultation" aria-label="Email for a free consultation">
  <button type="submit">Submit</button>
</form>

<svg style="position:absolute;left:0;top:0;pointer-events:none" width="1200" height="857" role="img" aria-label="Tilted screenshot of a search results page with news headlines and image thumbnails">
  <defs>
    <linearGradient id="shotFill" x1="0" y1="0" x2="1" y2="1">
      <stop offset="0" stop-color="#fdfdfd"/>
      <stop offset="1" stop-color="#e9ecf0"/>
    </linearGradient>
    <filter id="shotShadow" x="-10%" y="-10%" width="120%" height="130%">
      <feDropShadow dx="0" dy="8" stdDeviation="8" flood-color="#000" flood-opacity=".18"/>
    </filter>
  </defs>
  <polygon points="761,196 1159,158 1146,492 760,456" fill="url(#shotFill)" stroke="#ffffff" stroke-width="5" filter="url(#shotShadow)"/>
</svg>

<section class="contact-panel">
  <span class="divider" style="left:310px"></span>
  <span class="divider" style="left:634px"></span>

  <h2 class="panel-heading">Get in touch</h2>
  <div class="handset-art" role="img" aria-label="Mobile handset illustration"></div>
  <span class="talk-label">TALK TO US</span>
  <span class="contact-label" style="left:78px;top:60px">Phone</span>
  <span class="contact-value" style="left:78px;top:83px">(91) 55510-42786</span>

  <div class="mail-art" role="img" aria-label="Envelope illustration"></div>
  <span class="contact-label" style="left:421px;top:60px">Email Address</span>
  <span class="contact-value" style="left:419px;top:83px">info@quorvanemedia.com</span>

  <div class="share-row" style="top:44px">
    <span class="share-btn deep">SHARE</span>
    <span class="share-text">Sign in with Brellows.</span>
  </div>
  <div class="share-row" style="top:86px">
    <span class="share-btn light">SHARE</span>
    <span class="share-text">Sign in with Chirrup.</span>
  </div>
</section>

<footer class="site-footer">Quorvane Media, Copyright © 2012 | About Us ~ Support ~ FAQ's ~ Testimonials ~ Blog ~ Contact Us</footer>

</body>
</html>
```